Delia Forsby Space Tamer

a larger business card may standard size 4” x 9” describing what I do. I don’t know if this would be considered a flyer. I rearrange, redesign and stage houses for the owner or to sell.

```html
<!DOCTYPE html>
<html lang="en">
<head>
<meta charset="utf-8">
<title>Delia Forsby – Space Tamer card</title>
<link rel="stylesheet" href="https://fonts.googleapis.com/css2?family=Cinzel:wght@400;500&family=Sorts+Mill+Goudy:ital@0;1&family=Poppins:wght@400&display=swap">
<style>
  :root {
    --page: #ffffff;
    --card: #ffffff;
    --ink-soft: #a9b3c0;
    --ink-mid: #7f8894;
    --teal: #1f9187;
    --teal-wash: #9fd6d6;
    --sky-top: #3f6f9a;
    --sky-low: #8aa9bf;
    --adobe: #d8844f;
    --adobe-dark: #9a5a35;
    --ground: #7d8683;
    --white: #ffffff;
  }
  * { box-sizing: border-box; margin: 0; padding: 0; }
  html, body { width: 1200px; height: 1200px; overflow: hidden; background: var(--page); }
  .canvas { position: relative; width: 1200px; height: 1200px; }

  .card { position: absolute; background: var(--card); }
  .card-front { left: 53px; top: 45px; width: 1080px; height: 483px; }
  .card-rear { left: 51px; top: 627px; width: 1083px; height: 477px;
    background: linear-gradient(172deg, var(--card) 45%, #e4f3f3 68%, var(--teal-wash) 100%); }

  .hero { position: absolute; left: 37px; top: 36px; width: 999px; height: 409px;
    background:
      linear-gradient(180deg, var(--sky-top) 0%, var(--sky-low) 26%, #6e5a4c 34%, var(--adobe) 46%, var(--adobe) 70%, var(--adobe-dark) 86%, var(--ground) 100%); }
  .hero::before { content: ""; position: absolute; left: 0; top: 0; width: 30%; height: 100%;
    background: linear-gradient(90deg, rgba(58,88,48,.85), rgba(58,88,48,0)); }

  .hero-title { position: absolute; left: 0; right: 0; text-align: center; color: var(--white);
    font-family: "Cinzel", serif; font-weight: 400; line-height: 1; }
  .hero-first { top: 52px; font-size: 44px; letter-spacing: 2px; }
  .hero-last { top: 96px; font-size: 68px; letter-spacing: 2px; }
  .hero-role { top: 178px; font-size: 30px; letter-spacing: 2px; }
  .hero-role small { font-size: 22px; }
  .hero-tagline { position: absolute; left: 206px; top: 355px; color: var(--white);
    font-family: "Poppins", sans-serif; font-size: 20px; white-space: pre; }

  .portrait { position: absolute; left: 0; top: 25px; width: 129px; height: 164px;
    background: linear-gradient(180deg, #e8e4df 0%, #d9b8a6 45%, #c79a86 70%, #2aa39b 82%, #1f9187 100%); }

  .rear-copy { position: absolute; left: 156px; top: 78px; width: 900px; font-family: "Sorts Mill Goudy", serif; }
  .lead { color: var(--ink-soft); font-size: 33px; line-height: 40px; letter-spacing: 1.4px; }
  .bio { margin-top: 10px; color: var(--ink-soft); font-style: italic; font-size: 20.5px; line-height: 30px; }
  .pitch { margin-top: 12px; color: var(--teal); font-style: italic; font-size: 28.5px; line-height: 37px; }
  .contact { position: absolute; left: 153px; top: 406px; color: var(--ink-mid);
    font-family: "Sorts Mill Goudy", serif; font-size: 21px; letter-spacing: .6px; white-space: nowrap; }
  .contact .email { font-weight: 700; color: var(--ink-mid); }
  .contact span + span { margin-left: 10px; }
</style>
</head>
<body>
<main class="canvas">
  <section class="card card-front" aria-label="Card front">
    <div class="hero" role="img" aria-label="Photo of an adobe-style house with wooden garage doors, lanterns and desert mountains at dusk">
      <div class="hero-title hero-first">DELIA</div>
      <div class="hero-title hero-last">FORSBY</div>
      <div class="hero-title hero-role"><small>A</small> S<small>PACE</small> T<small>AMER</small></div>
      <div class="hero-tagline">Homes:  Rearranged. Redesigned. Staged to Sell.</div>
    </div>
  </section>

  <section class="card card-rear" aria-label="Card back">
    <div class="portrait" role="img" aria-label="Portrait photo of Delia Forsby"></div>
    <div class="rear-copy">
      <p class="lead">For 36 years, Delia was a real estate broker in Oregon. She has a track record of transforming houses that do not sell into homes that sell quickly.</p>
      <p class="bio">As a Hearth &amp; Garden Living national award winner, her talent has not gone unnoticed. She eargerly finds renewed energy by rearranging what you already have, and rethinking your space. With a dash of this, a zest of that, she virtually re-invigorates your environment.</p>
      <p class="pitch">Make your space livable, lovable and profitable… a place where you or your buyer can hardly wait to come home to. Voila!</p>
    </div>
    <p class="contact"><span class="email">deliaforsby@mailbay.net</span><span>503-555-0148</span><span>4120 West Marrow Lane, Yuma, AZ  85367</span></p>
  </section>
</main>
</body>
</html>
```